Website for Construction Company
Fire, Water, Mold, Storm
Project: Website for Construction Company
Website for Construction Company - Construction
Creative Brief
Construction
www.harborlinebuilders.com
Kestrel Ridge Builders has over 20 years experience in the construction business. Our company has a variety of experienced workers and subcontractors that provide services for banks, insurance companies, lenders, real estate agents, investors, and homeowners.Our services include, Fire Damage Restoration, Water Damage Restoration, Mold Remediation, Storm Damage Restoration, Smoke Damage Restoration, Vandalism Restoration, Remodeling, and home additions. REO services include, boarding/securing properties, Re-keying, clean out/trashouts, Property Inspections,Property winterizations etc.
I would like to see the Chatterloop, Work Weave, and Quippr links. NTA logo, orba, tollipay, coastal transfer, and wayfarer Credit cards accepted. We are licensed, bonded and insured. I would like to have client testimonials, request for free estimates,
Red
Green, Yellow
left side
http://www.quillmere-renewal.com/
http://www.hearthmend.com/
http://www.tamsenfold.com/
http://www.ok-revivals.com http://www.zelvamend.com/

```html
<!DOCTYPE html>
<html lang="en">
<head>
<meta charset="utf-8">
<title>Kestrel Ridge Builders – Home Restoration Specialists</title>
<link href="https://fonts.googleapis.com/css2?family=Oswald:wght@500;700&family=Open+Sans:wght@400;600;700&display=swap" rel="stylesheet">
<style>
:root{
  --ink:#2b2b2b;
  --muted:#555;
  --nav:#2a2a2a;
  --nav-top:#3d3d3d;
  --sky-top:#1d5fa3;
  --sky-bottom:#d9e2ea;
  --page:#e6e8ea;
  --panel:#ffffff;
  --blue:#1f73c4;
  --blue-dark:#184e86;
  --form:#1c4a78;
  --red:#d8262a;
  --green:#5aa52c;
  --yellow:#f2b01e;
  --orange:#e8811d;
  --footer:#2d2d2d;
  --line:#d3d7db;
}
*{box-sizing:border-box;margin:0;padding:0}
html,body{width:1200px;height:980px;overflow:hidden}
body{position:relative;background:var(--page);font-family:"Open Sans",Arial,sans-serif;color:var(--ink)}
.abs{position:absolute}

.site-header{left:0;top:0;width:1200px;height:92px;background:#fff}
.brand{left:190px;top:24px;display:flex;align-items:center;gap:10px}
.brand-mark{width:40px;height:40px;background:var(--blue);border-radius:6px}
.brand-name{font-weight:700;font-size:23px;color:var(--blue-dark);line-height:1}
.brand-tag{font-size:11px;color:var(--muted);margin-top:4px;padding-left:52px}
.phone{left:725px;top:40px;display:flex;align-items:center;gap:8px;font-size:22px;color:var(--blue);font-weight:600}
.assoc-badge{left:905px;top:26px;width:104px;height:46px;background:var(--blue-dark);border-radius:4px}

.main-nav{left:0;top:92px;width:1200px;height:38px;background:linear-gradient(var(--nav-top),var(--nav))}
.main-nav ul{list-style:none;display:flex;gap:29px;padding-left:208px;height:38px;align-items:center}
.main-nav a{color:#fff;text-decoration:none;font-size:13.5px}

.sky{left:0;top:130px;width:1200px;height:320px;background:linear-gradient(var(--sky-top),#6d9ac6 60%,var(--sky-bottom))}

.content{left:188px;top:148px;width:824px;height:690px;background:var(--panel);border-radius:8px;box-shadow:0 2px 8px rgba(0,0,0,.25)}

.hero{left:200px;top:156px;width:596px;height:264px;border-radius:6px;background:linear-gradient(#c4d4df,#b98e6e 55%,#7a8f6c);overflow:hidden}
.hero-title{left:18px;top:86px;font-family:"Oswald",Impact,sans-serif;font-weight:700;color:#fff;font-size:50px;line-height:56px;text-shadow:0 2px 4px rgba(0,0,0,.5)}
.hero-btn{left:22px;top:206px;background:var(--green);color:#fff;font-size:12px;font-weight:700;padding:5px 14px;border-radius:3px}
.hero-dots{left:22px;top:244px;display:flex;gap:6px}
.hero-dots i{width:8px;height:8px;border-radius:50%;background:#fff;opacity:.6}
.hero-dots i:first-child{opacity:1}

.estimate{left:800px;top:156px;width:204px;height:264px;background:var(--form);border-radius:6px}
.estimate h2{position:absolute;left:8px;top:6px;width:204px;height:30px;background:var(--red);color:#fff;font-size:13px;font-weight:600;line-height:30px;text-align:center;border-radius:3px 0 0 3px}
.field{position:absolute;left:20px;width:164px;height:26px;background:#fff;border-radius:3px;font-size:11px;padding:5px 8px;color:#333}
.estimate .submit{position:absolute;left:20px;top:220px;background:var(--yellow);color:#222;font-size:11px;font-weight:700;padding:6px 12px;border-radius:3px}

.services{left:200px;top:430px;width:804px;display:flex;gap:8px}
.service{width:195px;height:132px;position:relative}
.service-photo{height:96px;border-radius:4px 4px 0 0}
.service-label{height:34px;background:linear-gradient(var(--blue),var(--blue-dark));color:#fff;font-family:"Oswald",Impact,sans-serif;font-weight:500;font-size:18px;line-height:34px;padding-left:14px}
.water{background:linear-gradient(#7d8e6a,#4f6b52)}
.fire{background:linear-gradient(#6b7f99,#3c3a38)}
.smoke{background:linear-gradient(#8fa0b8,#5e5a57)}
.mold{background:linear-gradient(#5b4a36,#2f2a22)}

.info-box{top:600px;width:262px;height:218px;border:1px solid var(--line);border-radius:4px;background:#fff}
.info-box h3{position:absolute;left:-1px;top:-6px;width:200px;height:28px;background:var(--blue);color:#fff;font-size:13.5px;font-weight:600;line-height:28px;padding-left:18px;border-radius:0 3px 3px 0}
.emergency{left:202px}
.testimonials{left:470px}
.why{left:738px}
.map{position:absolute;left:42px;top:36px;width:178px;height:96px;background:linear-gradient(#f4f4f4,#d9d9d9);border-radius:4px}
.emergency p{position:absolute;left:0;top:146px;width:262px;text-align:center;font-size:11.5px}
.zip{position:absolute;left:64px;top:172px;width:112px;height:22px;border:1px solid #bbb;font-size:10px;padding:4px 8px;color:#666}
.go{position:absolute;left:178px;top:172px;width:28px;height:22px;background:var(--blue);color:#fff;font-size:10px;font-weight:700;text-align:center;line-height:22px}
.avatar{position:absolute;left:22px;top:40px;width:42px;height:42px;background:#9b6b8a;border-radius:3px}
.quote{position:absolute;left:74px;top:40px;width:176px;font-size:11.5px;line-height:15px;color:#333}
.quote cite{display:block;font-style:normal;margin-top:4px}
.read-all{position:absolute;left:24px;top:164px;font-size:10.5px;font-weight:700;color:var(--orange)}
.video{position:absolute;left:26px;top:36px;width:212px;height:122px;background:linear-gradient(#a5623b,#5a3520);border-radius:3px}
.video svg{position:absolute;left:86px;top:41px}
.why p{position:absolute;left:24px;top:166px;width:214px;text-align:center;font-size:11.5px;line-height:16px}

.site-footer{left:0;top:846px;width:1200px;height:86px;background:var(--footer);color:#fff}
.footer-col{position:absolute;top:10px;font-size:11.5px;font-weight:600}
.assoc{left:218px}
.assoc .badge{width:104px;height:42px;background:var(--blue-dark);border-radius:4px;margin-top:8px}
.pay{left:484px}
.pay ul,.social ul{list-style:none;display:flex;gap:6px;margin-top:10px}
.pay li{background:#fff;color:var(--ink);font-size:9.5px;font-weight:600;padding:0 6px;height:30px;line-height:30px;border-radius:3px}
.social{left:868px}
.social li{font-size:10.5px;font-weight:600}

.copyright{left:188px;top:942px;font-size:11px;color:var(--muted)}
</style>
</head>
<body>

<header class="site-header abs">
  <div class="brand abs">
    <span class="brand-mark"></span>
    <span class="brand-name">Kestrel Ridge Builders</span>
  </div>
  <div class="brand-tag abs" style="left:190px;top:64px">Home Restoration Specialists</div>
  <div class="phone abs">
    <svg width="18" height="20" viewBox="0 0 18 20" aria-hidden="true"><path d="M4 1l3 4-2 2c1 3 3 5 6 7l2-2 4 3-2 4C8 18 1 11 1 4z" fill="var(--blue)"/></svg>
    888-555-0142
  </div>
  <div class="assoc-badge abs" role="img" aria-label="Accredited business badge"></div>
</header>

<nav class="main-nav abs">
  <ul>
    <li><a href="#">Home</a></li>
    <li><a href="#">About Us</a></li>
    <li><a href="#">Restoration Services</a></li>
    <li><a href="#">construction &amp; Remodeling</a></li>
    <li><a href="#">Photo Gallery</a></li>
    <li><a href="#">News</a></li>
    <li><a href="#">Testimonials</a></li>
    <li><a href="#">Contact Us</a></li>
  </ul>
</nav>

<div class="sky abs"></div>
<main class="content abs"></main>

<section class="hero abs" role="img" aria-label="Photo of a flooded suburban house">
  <h1 class="hero-title abs">GOT DAMAGE?<br>GET HELP FAST</h1>
  <span class="hero-btn abs">CONTACT US TODAY</span>
  <div class="hero-dots abs"><i></i><i></i><i></i></div>
</section>

<form class="estimate abs">
  <h2>Request for free estimates</h2>
  <div class="field" style="top:50px">Full Name</div>
  <div class="field" style="top:82px">Email</div>
  <div class="field" style="top:114px">Phone</div>
  <div class="field" style="top:146px;height:58px">Comment</div>
  <span class="submit">Get your Estimate</span>
</form>

<section class="services abs">
  <div class="service"><div class="service-photo water" role="img" aria-label="Photo of a flooded room"></div><div class="service-label">WATER DAMAGE</div></div>
  <div class="service"><div class="service-photo fire" role="img" aria-label="Photo of a house on fire"></div><div class="service-label">FIRE DAMAGE</div></div>
  <div class="service"><div class="service-photo smoke" role="img" aria-label="Photo of smoke rising from a building"></div><div class="service-label">SMOKE DAMAGE</div></div>
  <div class="service"><div class="service-photo mold" role="img" aria-label="Photo of mold on a wall"></div><div class="service-label">MOLD DAMAGE</div></div>
</section>

<section class="info-box emergency abs">
  <h3>Need Emergency Service?</h3>
  <div class="map" role="img" aria-label="Map of the United States"></div>
  <p>Contact us for 24 hour emergency</p>
  <div class="zip">Enter Zip code</div>
  <div class="go">GO</div>
</section>

<section class="info-box testimonials abs">
  <h3>Client Testimonials</h3>
  <div class="avatar" role="img" aria-label="Client portrait"></div>
  <blockquote class="quote">Great work by all, attention to detail and everyone was very professional. Would recommend your company to anyone in need of your services
    <cite>Rina Okafor</cite></blockquote>
  <span class="read-all">READ ALL »</span>
</section>

<section class="info-box why abs">
  <h3>Why Choose Us?</h3>
  <div class="video" role="img" aria-label="Video still of a restored interior">
    <svg width="40" height="40" viewBox="0 0 40 40" aria-hidden="true"><circle cx="20" cy="20" r="19" fill="rgba(0,0,0,.45)"/><path d="M15 11l14 9-14 9z" fill="#fff"/></svg>
  </div>
  <p>Lorem Ipsum is simply dummy text of the printing and typesetting industry</p>
</section>

<footer class="site-footer abs">
  <div class="footer-col assoc">Associated with
    <div class="badge" role="img" aria-label="NTA accreditation badge"></div>
  </div>
  <div class="footer-col pay">We Accepted
    <ul><li>orba</li><li>tollipay</li><li>coastal transfer</li><li>wayfarer</li></ul>
  </div>
  <div class="footer-col social">Connect with us
    <ul><li>Quippr</li><li>Chatterloop</li><li>Work Weave</li></ul>
  </div>
</footer>

<p class="copyright abs">Copyrights @2012 Kestrel Ridge Builders. All rights reserved.</p>

</body>
</html>
```